Bright Path Therapies business cards and stationary

Need business cards and stationary designed to match previously made logo for for a new company based in Sydney NSW called 'Bright Path Therapies'.

We provide early intervention services and diagnostic assessment for children with disability and their families. I would like designs that are colourful and child friendly - possibly using feet/footprints/steps on a white background. The final design should communicate that we are family friendly, accepting and fun to work with.

Target Market(s)

Parents and Families
Teachers
Allied Health Professionals

Industry/Entity Type

Psychology

Contact Information for Business Card

Bright Path Therapies
www.brightpaththerapies.example
info@brightpaththerapies.example

Font styles to use
Sans Serif
Decorative
Script

Requirements
Must have
• Match the font and colour scheme of logo, along with footprint picture
Nice to have
• Clean and simple, while reflecting that I am working with families.
• Also- editable for when we make staff specific cards.

```html
<!DOCTYPE html>
<html lang="en">
<head>
<meta charset="utf-8">
<title>Bright Path Therapies – Business Card</title>
<link rel="stylesheet" href="https://fonts.googleapis.com/css2?family=Nunito:wght@600;700;800&display=swap">
<style>
  :root {
    --page: #e4e4e4;
    --card: #fbfbfb;
    --ink-dark: #2e2e2e;
    --blue: #1a75bb;
    --red: #d8362b;
    --green: #7ab530;
    --orange: #e07d22;
    --white: #ffffff;
  }
  * { box-sizing: border-box; margin: 0; padding: 0; }
  html, body {
    width: 1200px; height: 576px; overflow: hidden;
    background: var(--page);
    font-family: "Nunito", sans-serif;
  }
  .stage { position: relative; width: 1200px; height: 576px; }

  .card {
    position: absolute; top: 138px;
    width: 484px; height: 294px;
    border-radius: 14px; overflow: hidden;
    background: var(--card);
  }
  .card--front { left: 82px; }
  .card--back { left: 602px; background: var(--white); }

  /* Front */
  .corner-prints {
    position: absolute; width: 62px; height: 86px; border-radius: 0 0 18px 0;
    background: linear-gradient(160deg, rgba(26,117,187,.22), rgba(216,54,43,.2) 45%, rgba(122,181,48,.22));
  }
  .corner-prints--top { left: 0; top: 0; }
  .corner-prints--bottom {
    right: 0; bottom: 7px; width: 62px; height: 82px; border-radius: 18px 0 0 0;
    background: linear-gradient(160deg, rgba(224,125,34,.24), rgba(26,117,187,.22) 55%, rgba(122,181,48,.22));
  }

  .brand {
    position: absolute; left: 0; right: 0; top: 116px;
    display: flex; align-items: center; justify-content: center; gap: 14px;
  }
  .brand__dot { width: 48px; height: 48px; border-radius: 50%; background: var(--red); }
  .brand__name { font-size: 28px; font-weight: 800; color: var(--blue); letter-spacing: .3px; }

  .color-band { position: absolute; left: 0; right: 0; bottom: 0; height: 7px; display: flex; }
  .color-band span { flex: 1; }
  .color-band .blue { background: var(--blue); }
  .color-band .red { background: var(--red); }
  .color-band .green { background: var(--green); }
  .color-band .orange { background: var(--orange); }

  /* Back */
  .footprint-field {
    position: absolute; inset: 0;
    background: linear-gradient(115deg,
      rgba(216,54,43,.28) 0%,
      rgba(224,125,34,.26) 30%,
      rgba(122,181,48,.24) 60%,
      rgba(26,117,187,.28) 100%);
  }
  .contact-oval {
    position: absolute; left: 102px; top: 16px;
    width: 278px; height: 236px; border-radius: 50%;
    background: var(--ink-dark);
    display: flex; flex-direction: column; align-items: center; justify-content: center;
    text-align: center;
  }
  .contact-oval__name {
    font-size: 22px; font-weight: 800; color: var(--blue);
    letter-spacing: .3px; margin-top: -4px; margin-bottom: 30px;
  }
  .contact-oval__email { font-size: 12.5px; font-weight: 600; color: var(--white); margin-bottom: 5px; }
  .contact-oval__web { font-size: 12.5px; font-weight: 700; }
  .contact-oval__web .c-red { color: var(--red); }
  .contact-oval__web .c-orange { color: var(--orange); }
  .contact-oval__web .c-green { color: var(--green); }
  .contact-oval__web .c-blue { color: var(--blue); }
  .contact-oval__web .c-white { color: var(--white); }
</style>
</head>
<body>
<main class="stage">
  <section class="card card--front">
    <div class="corner-prints corner-prints--top" role="img" aria-label="Faint coloured footprints in the top corner"></div>
    <div class="corner-prints corner-prints--bottom" role="img" aria-label="Faint coloured footprints in the bottom corner"></div>
    <div class="brand">
      <span class="brand__dot"></span>
      <span class="brand__name">Bright Path Therapies</span>
    </div>
    <div class="color-band">
      <span class="blue"></span><span class="red"></span><span class="green"></span><span class="orange"></span>
    </div>
  </section>

  <section class="card card--back">
    <div class="footprint-field" role="img" aria-label="Scattered colourful footprints and dots in red, orange, green and blue"></div>
    <div class="contact-oval">
      <p class="contact-oval__name">Bright Path Therapies</p>
      <p class="contact-oval__email">info@brightpaththerapies.example</p>
      <p class="contact-oval__web"><span class="c-white">www.</span><span class="c-red">bright</span><span class="c-orange">path</span><span class="c-green">thera</span><span class="c-blue">pies</span><span class="c-white">.example</span></p>
    </div>
  </section>
</main>
</body>
</html>
```